Norvane Builders Business Card

Modern and Professional Business Card for a Med size construction/development company.

See the samples below for the design I like … but I need ideas for incorporating the red company logo while still keeping the clean look of the card samples that are attached.

Logo and tag line on the back … info on the front.

Tagline: Quality Starts from the Ground Up

Target Market(s)

Med-Large General Contractors

Contact Information for Business Card

Norvane Builders Limited
42 Brenton Street
Elk Harbour, NL
B3K 7T2

t: 709-555-0147
f: 709-555-0192
w: www.norvanebuilders-example.com

Font styles to use
Sans Serif

Colors
fbee3e

Requirements
Must have
• I like the black and yellow designs of the attached samples …. but I'm not sure how to incorporate the red Norvane Builders logo into that design??
Nice to have
• Construction safety strips

```html
<!DOCTYPE html>
<html lang="en">
<head>
<meta charset="utf-8">
<title>Norvane Builders Business Card</title>
<link href="https://fonts.googleapis.com/css2?family=Open+Sans:wght@400;600;700;800&display=swap" rel="stylesheet">
<style>
  :root {
    --brand-red: #e31e25;
    --brand-yellow: #fbee3e;
    --brand-black: #1c1c1c;
    --card-white: #ffffff;
    --text-grey: #5a5a5a;
    --backdrop: #d9d9db;
    --shadow: rgba(0, 0, 0, 0.22);
  }
  * { margin: 0; padding: 0; box-sizing: border-box; }
  html, body {
    width: 1200px;
    height: 913px;
    overflow: hidden;
    background: var(--backdrop);
    font-family: "Open Sans", Arial, sans-serif;
  }
  .stage {
    position: relative;
    width: 1200px;
    height: 913px;
  }
  .card {
    position: absolute;
    width: 620px;
    height: 354px;
    border-radius: 26px;
    box-shadow: 0 14px 30px var(--shadow);
    overflow: hidden;
  }

  /* Back side: name block and tagline */
  .card-back {
    left: 70px;
    top: 70px;
    background: var(--brand-red);
    color: var(--card-white);
    display: flex;
    flex-direction: column;
    align-items: center;
  }
  .brand-block {
    margin-top: 92px;
    display: flex;
    flex-direction: column;
    align-items: center;
  }
  .brand-name {
    color: var(--brand-black);
    font-weight: 800;
    font-size: 54px;
    letter-spacing: 1px;
    text-transform: uppercase;
    line-height: 1;
  }
  .brand-rule {
    width: 360px;
    height: 3px;
    background: var(--brand-yellow);
    margin: 14px 0 10px;
  }
  .brand-suffix {
    color: var(--brand-black);
    font-weight: 800;
    font-size: 20px;
    letter-spacing: 7px;
    text-transform: uppercase;
  }
  .brand-rule-lower {
    width: 300px;
    height: 3px;
    background: var(--brand-yellow);
    margin-top: 10px;
  }
  .tagline {
    margin-top: auto;
    margin-bottom: 58px;
    font-size: 17px;
    font-weight: 400;
    letter-spacing: 1px;
    text-transform: uppercase;
  }

  /* Front side: contact info */
  .card-front {
    left: 510px;
    top: 489px;
    background: var(--card-white);
  }
  .front-mark {
    position: absolute;
    top: 32px;
    right: 34px;
    color: var(--brand-black);
    font-weight: 800;
    font-size: 28px;
    text-transform: uppercase;
    letter-spacing: 0.5px;
  }
  .front-mark-rule {
    position: absolute;
    top: 76px;
    right: 34px;
    width: 250px;
    height: 3px;
    background: var(--brand-yellow);
  }
  .contact {
    position: absolute;
    left: 40px;
    bottom: 36px;
    color: var(--text-grey);
    font-size: 17px;
    line-height: 1.35;
  }
  .contact-name {
    color: var(--brand-red);
    font-weight: 600;
    font-size: 19px;
  }
  .contact-address { margin-bottom: 12px; }
  .contact-line {
    display: flex;
    align-items: center;
    gap: 8px;
  }
  .contact-icon {
    width: 15px;
    height: 15px;
    flex: none;
  }
</style>
</head>
<body>
  <main class="stage">
    <section class="card card-back" aria-label="Card back">
      <div class="brand-block">
        <div class="brand-name">Norvane Builders</div>
        <div class="brand-rule"></div>
        <div class="brand-suffix">Limited</div>
        <div class="brand-rule-lower"></div>
      </div>
      <p class="tagline">Quality Starts from the Ground Up</p>
    </section>

    <section class="card card-front" aria-label="Card front">
      <div class="front-mark">Norvane Builders</div>
      <div class="front-mark-rule"></div>
      <div class="contact">
        <div class="contact-name">Norvane Builders Limited</div>
        <div class="contact-address">
          42 Brenton Street<br>
          Elk Harbour, NL, B3K 7T2
        </div>
        <div class="contact-line">
          <svg class="contact-icon" viewBox="0 0 16 16" aria-hidden="true">
            <path fill="#e31e25" d="M3.2 1.5l2.3-.4 1.3 3.2-1.5 1.1c.8 1.8 2 3 3.8 3.8l1.1-1.5 3.2 1.3-.4 2.3c-.2.9-1 1.5-1.9 1.4C6 12.3 3.7 10 3.3 4.4c-.1-.9.5-1.7 1.4-1.9z"/>
          </svg>
          <span>709-555-0147</span>
        </div>
        <div class="contact-line">
          <svg class="contact-icon" viewBox="0 0 16 16" aria-hidden="true">
            <rect x="4" y="1.5" width="8" height="4" fill="none" stroke="#e31e25" stroke-width="1.5"/>
            <rect x="1.5" y="5.5" width="13" height="6" rx="1" fill="#e31e25"/>
            <rect x="4" y="9.5" width="8" height="5" fill="#fff" stroke="#e31e25" stroke-width="1.5"/>
          </svg>
          <span>709-555-0192</span>
        </div>
        <div class="contact-line">
          <svg class="contact-icon" viewBox="0 0 16 16" aria-hidden="true">
            <circle cx="8" cy="8" r="6.5" fill="none" stroke="#e31e25" stroke-width="1.5"/>
            <ellipse cx="8" cy="8" rx="2.8" ry="6.5" fill="none" stroke="#e31e25" stroke-width="1.2"/>
            <line x1="1.5" y1="8" x2="14.5" y2="8" stroke="#e31e25" stroke-width="1.2"/>
          </svg>
          <span>www.norvanebuilders-example.com</span>
        </div>
      </div>
    </section>
  </main>
</body>
</html>
```